Ridgeline Talent Associates Business Card Design

We need a business card design for our new company - Ridgeline Talent Associates. RLTA is a recruitment firm that focuses on recruiting engineers and geologist for mid-size oil and gas companies. We would like our logo on the business card, which is attached, and we would like the color scheme on business cards to coordinate with our logo.

Industry/Entity Type

Oil And Gas

Contact Information for Business Card

Dana Whitfield, Founder and Managing Partner, dmw@ridgelinetalentco.org, 888.574.2093 (work), 8140395.0611 (cell), 814.527.6730 (fax), www.ridgelinetalentco.org

```html
<!DOCTYPE html>
<html lang="en">
<head>
<meta charset="utf-8">
<title>Ridgeline Talent Associates – Business Card</title>
<link rel="stylesheet" href="https://fonts.googleapis.com/css2?family=Orbitron:wght@400;600&display=swap">
<style>
  :root {
    --page-bg: #e6e4e0;
    --card-white: #f4f4f4;
    --card-highlight: #ffffff;
    --edge-gray: #4b4c4e;
    --band-navy: #2f3059;
    --ink-dark: #2b2b2b;
    --icon-bg: #3a3a3c;
    --logo-navy: #2c3a6e;
  }
  * { box-sizing: border-box; margin: 0; padding: 0; }
  html, body {
    width: 1200px;
    height: 1019px;
    overflow: hidden;
    background: var(--page-bg);
  }
  .business-card {
    position: absolute;
    left: 350px;
    top: 80px;
    width: 500px;
    height: 860px;
    background: radial-gradient(ellipse at 55% 30%, var(--card-highlight), var(--card-white) 70%);
    box-shadow: 0 10px 30px rgba(0,0,0,0.18);
    overflow: hidden;
    font-family: "Orbitron", "Arial", sans-serif;
  }
  .edge-strip {
    position: absolute;
    top: 0;
    width: 34px;
    height: 100%;
    background: var(--edge-gray);
  }
  .edge-strip--left { left: 0; }
  .edge-strip--right { right: 0; }

  .company-mark {
    position: absolute;
    top: 210px;
    left: 34px;
    right: 34px;
    display: flex;
    align-items: center;
    justify-content: center;
    gap: 12px;
  }
  .company-mark__dot {
    width: 22px;
    height: 22px;
    border-radius: 50%;
    background: var(--logo-navy);
    flex: none;
  }
  .company-mark__name {
    font-size: 17px;
    font-weight: 600;
    color: var(--logo-navy);
    letter-spacing: 0.02em;
  }

  .name-band {
    position: absolute;
    top: 345px;
    left: 34px;
    right: 34px;
    height: 135px;
    padding: 0 16px;
    background: var(--band-navy);
    display: flex;
    flex-direction: column;
    align-items: center;
    justify-content: center;
    color: #fff;
    text-transform: uppercase;
    text-align: center;
  }
  .name-band__name {
    font-size: 30px;
    font-weight: 400;
    letter-spacing: 0.06em;
    white-space: nowrap;
  }
  .name-band__title {
    margin-top: 12px;
    font-size: 15px;
    font-weight: 400;
    letter-spacing: 0.05em;
    white-space: nowrap;
  }

  .contact-list {
    position: absolute;
    top: 520px;
    left: 34px;
    right: 34px;
    list-style: none;
  }
  .contact-list__item {
    display: flex;
    align-items: center;
    height: 48px;
    margin-bottom: 6px;
  }
  .contact-list__icon {
    width: 40px;
    height: 40px;
    border-radius: 0 6px 6px 0;
    background: var(--icon-bg);
    display: flex;
    align-items: center;
    justify-content: center;
    flex: none;
  }
  .contact-list__icon svg { width: 22px; height: 22px; }
  .contact-list__text {
    margin-left: 16px;
    font-size: 16px;
    color: var(--ink-dark);
    letter-spacing: 0.02em;
    white-space: nowrap;
  }
</style>
</head>
<body>
  <article class="business-card">
    <div class="edge-strip edge-strip--left"></div>
    <div class="edge-strip edge-strip--right"></div>

    <div class="company-mark">
      <span class="company-mark__dot"></span>
      <span class="company-mark__name">Ridgeline Talent Associates</span>
    </div>

    <header class="name-band">
      <h1 class="name-band__name">Dana Whitfield</h1>
      <p class="name-band__title">Founder and Managing Partner</p>
    </header>

    <ul class="contact-list">
      <li class="contact-list__item">
        <span class="contact-list__icon">
          <svg viewBox="0 0 24 24"><path fill="#fff" d="M6.6 10.8a15 15 0 0 0 6.6 6.6l2.2-2.2c.3-.3.7-.4 1-.2 1.1.4 2.3.6 3.6.6.6 0 1 .4 1 1V20c0 .6-.4 1-1 1A17 17 0 0 1 3 4c0-.6.4-1 1-1h3.5c.6 0 1 .4 1 1 0 1.3.2 2.5.6 3.6.1.3 0 .7-.2 1z"/></svg>
        </span>
        <span class="contact-list__text">888.574.2093</span>
      </li>
      <li class="contact-list__item">
        <span class="contact-list__icon">
          <svg viewBox="0 0 24 24"><rect x="7" y="2" width="10" height="20" rx="2" fill="none" stroke="#fff" stroke-width="2"/><circle cx="12" cy="18" r="1.2" fill="#fff"/></svg>
        </span>
        <span class="contact-list__text">8140395.0611</span>
      </li>
      <li class="contact-list__item">
        <span class="contact-list__icon">
          <svg viewBox="0 0 24 24"><rect x="7" y="3" width="10" height="6" fill="#fff"/><rect x="3" y="9" width="18" height="9" rx="1.5" fill="#fff"/><rect x="7" y="15" width="10" height="6" fill="#fff" stroke="#3a3a3c" stroke-width="1.2"/></svg>
        </span>
        <span class="contact-list__text">814.527.6730</span>
      </li>
      <li class="contact-list__item">
        <span class="contact-list__icon">
          <svg viewBox="0 0 24 24"><rect x="3" y="6" width="18" height="12" fill="#fff"/><path d="M3 6l9 7 9-7" fill="none" stroke="#3a3a3c" stroke-width="1.5"/></svg>
        </span>
        <span class="contact-list__text">dmw@ridgelinetalentco.org</span>
      </li>
      <li class="contact-list__item">
        <span class="contact-list__icon">
          <svg viewBox="0 0 24 24" fill="none" stroke="#fff" stroke-width="1.6"><circle cx="12" cy="12" r="9"/><ellipse cx="12" cy="12" rx="4" ry="9"/><path d="M3 12h18M5 7h14M5 17h14"/></svg>
        </span>
        <span class="contact-list__text">www.ridgelinetalentco.org</span>
      </li>
      <li class="contact-list__item">
        <span class="contact-list__icon">
          <svg viewBox="0 0 24 24"><path fill="#fff" d="M12 2a7 7 0 0 0-7 7c0 5 7 13 7 13s7-8 7-13a7 7 0 0 0-7-7z"/><circle cx="12" cy="9" r="2.6" fill="#3a3a3c"/></svg>
        </span>
        <span class="contact-list__text">410 Ridge Road, Suite 18</span>
      </li>
    </ul>
  </article>
</body>
</html>
```